Web design - holistic filmmaker

I need a design for my new website.

I am a holistic filmmaker, ie I make films for healers, alternative practitioners, spiritual people and institutions that offer training in this field.

The design should be noble, bright, convey the feeling of space and expanse and have some particularly beautiful color accents.

The structure is: start page, offer, references, about me, imprint.

As an idea for the start page, I thought that either I could introduce myself as a filmmaker and my offer, or we could start right on the start page with the references, ie photos and links to already realized projects.

If you want more information or an exchange, I'd love to hear from you. At the moment I just don't know how to describe it better.

The winner will then be asked to design a logo.

Target Market(s)

healers, alternative practitioners, spiritual people and institutions that offer training in this field

Industry/Entity Type

Film production

Number of Pages Required

3 page

```html
<!DOCTYPE html>
<html lang="en">
<head>
<meta charset="utf-8">
<title>Jonas Reller – Films for the open-hearted</title>
<link href="https://fonts.googleapis.com/css2?family=Poppins:ital,wght@0,300;0,400;0,500;0,600;0,700;1,700&display=swap" rel="stylesheet">
<style>
:root{
  --cream:#fcf6ee;
  --white:#ffffff;
  --ink:#1f1d1b;
  --text:#444140;
  --muted:#5c5855;
  --accent:#e8456b;
  --footer:#2e2c2a;
  --footer-text:#f1ece6;
  --play:#e2231a;
}
*{margin:0;padding:0;box-sizing:border-box}
html,body{width:1200px;height:2747px;overflow:hidden}
body{position:relative;background:var(--white);font-family:'Poppins',sans-serif;color:var(--ink)}
.abs{position:absolute}
.btn{position:absolute;display:flex;align-items:center;justify-content:center;border:1.5px solid #3a3735;color:var(--ink);font-weight:500;text-transform:uppercase;text-decoration:none;background:transparent}

/* hero */
.hero{left:0;top:0;width:1200px;height:760px;background:var(--cream);overflow:hidden}
.flower{left:-120px;top:92px;width:388px;height:668px}
.portrait{left:630px;top:96px;width:570px;height:664px;border-radius:48% 40% 0 0/30% 26% 0 0;background:linear-gradient(160deg,#c9c5c0 0%,#b69077 35%,#e6852a 62%,#6d6a67 100%)}
.brand{left:103px;top:22px;display:flex;align-items:center;gap:14px}
.brand-dot{width:44px;height:44px;border-radius:50%;border:2px solid var(--ink)}
.brand-name{font-size:50px;font-weight:400;line-height:1;letter-spacing:.5px}
.brand-tag{font-size:16.5px;font-weight:400;color:var(--muted);margin-top:4px}
.nav{right:110px;top:47px;display:flex;gap:30px;font-size:20px;font-weight:400}
.nav a{color:var(--ink);text-decoration:none}
.nav a.active{color:var(--accent)}
.hero-copy{left:300px;top:204px}
.hero-copy .intro{font-size:45px;font-weight:600;line-height:1.2}
.hero-copy .name{font-size:88px;font-weight:700;font-style:italic;line-height:1.1;letter-spacing:-1px}
.hero-copy .role{font-size:45px;font-weight:600;line-height:1.3;margin-top:14px}
.hero-copy .lead{font-size:23.5px;color:var(--text);line-height:1.55;margin-top:26px}
.hero .btn{left:298px;top:565px;width:181px;height:66px;font-size:20px}

.torn{position:absolute;left:0;width:1200px}

/* works */
.section-title{position:absolute;left:0;width:1200px;text-align:center;font-size:45px;font-weight:600}
.work{position:absolute;overflow:hidden}
.work .play{position:absolute;left:50%;top:50%;width:78px;height:56px;margin:-28px 0 0 -39px;border-radius:14px;background:var(--play);opacity:.85}
.work .play::after{content:"";position:absolute;left:31px;top:17px;border-left:20px solid #fff;border-top:11px solid transparent;border-bottom:11px solid transparent}
.w1{left:111px;top:931px;width:306px;height:203px;background:linear-gradient(120deg,#6b4a3c,#c49a86 45%,#c54a8a 75%,#6a5a50)}
.w2{left:417px;top:906px;width:365px;height:254px;background:linear-gradient(140deg,#5f6b46,#8b8c6e 40%,#d1a08f 60%,#b6303f 100%);z-index:2}
.w2 .play{width:96px;height:68px;margin:-34px 0 0 -48px}
.w2 .play::after{left:38px;top:21px;border-left:24px solid #fff;border-top:13px solid transparent;border-bottom:13px solid transparent}
.w3{left:782px;top:931px;width:306px;height:203px;background:linear-gradient(180deg,#5e8fc5,#a9c7e3 55%,#5a4a40)}
.w4{left:1106px;top:931px;width:94px;height:203px;background:linear-gradient(180deg,#e2e0da,#c9c4ba);opacity:.7}
.works-btn{left:530px;top:1211px;width:139px;height:54px;font-size:18px}

/* journey */
.journey{left:0;top:1323px;width:1200px;height:597px;background:var(--cream);overflow:hidden}
.splash{left:587px;top:0;width:613px;height:597px;background:linear-gradient(180deg,#5fb6e0 0%,#f4ec2a 22%,#d61ec6 38%,#2e2fd0 60%,#1aa34a 75%,#ef2f7a 88%,#ff1d2a 100%);-webkit-mask-image:linear-gradient(90deg,transparent 0%,#000 45%);mask-image:linear-gradient(90deg,transparent 0%,#000 45%)}
.journey h2{position:absolute;left:107px;top:104px;font-size:47px;font-weight:600;line-height:1.2}
.journey p{position:absolute;left:111px;width:480px;font-size:17.5px;font-weight:300;color:var(--text);line-height:1.57}
.journey .p1{top:250px}
.journey .p2{top:360px}
.journey .btn{left:111px;top:461px;width:139px;height:54px;font-size:18px}

/* customers */
.clients{left:150px;top:2112px;width:900px;height:140px;display:flex;justify-content:space-around;align-items:center}
.client{display:flex;align-items:center;gap:10px;font-size:24px;font-weight:500;color:#3a3735}
.client-mark{width:16px;height:16px;border-radius:50%;background:var(--accent)}

/* footer */
.footer{left:0;top:2331px;width:1200px;height:416px;background:var(--footer);color:var(--footer-text)}
.footer .brand{left:107px;top:68px}
.footer .brand-dot{border-color:var(--footer-text)}
.footer .brand-name{font-size:50px}
.footer .brand-tag{color:var(--footer-text);font-size:17.5px}
.footer h4{position:absolute;top:94px;font-size:20.5px;font-weight:500}
.links{left:575px;top:138px;list-style:none;font-size:17px;line-height:32.5px}
.contact{left:772px;top:138px;list-style:none;font-size:17px;line-height:24px}
.contact li{display:flex;gap:8px;margin-bottom:25px}
.contact svg{flex:none;margin-top:5px}
.divider{left:111px;top:327px;width:978px;height:1px;background:#6c6864}
.copy{left:0;top:357px;width:1200px;text-align:center;font-size:16.5px}
</style>
</head>
<body>

<section class="hero abs">
  <svg class="flower abs" viewBox="0 0 388 668" role="img" aria-label="Rainbow flower of life ornament">
    <defs>
      <linearGradient id="rainbow" x1="0" y1="0" x2="0" y2="1">
        <stop offset="0" stop-color="#7a3fa0"/><stop offset=".2" stop-color="#e0342f"/>
        <stop offset=".4" stop-color="#f2a91c"/><stop offset=".5" stop-color="#c6d82a"/>
        <stop offset=".62" stop-color="#2fb4a8"/><stop offset=".8" stop-color="#e7532a"/>
        <stop offset="1" stop-color="#8a3aa0"/>
      </linearGradient>
    </defs>
    <circle cx="60" cy="380" r="322" fill="none" stroke="url(#rainbow)" stroke-width="8"/>
    <circle cx="60" cy="380" r="300" fill="url(#rainbow)" opacity=".35"/>
  </svg>
  <div class="portrait abs" role="img" aria-label="Portrait photo of the filmmaker in an orange shirt"></div>

  <div class="brand abs">
    <span class="brand-dot"></span>
    <div><div class="brand-name">Jonas Reller</div><div class="brand-tag">Films for the open-hearted</div></div>
  </div>
  <nav class="nav abs">
    <a class="active" href="#">Home</a><a href="#">Offer</a><a href="#">References</a><a href="#">About me</a><a href="#">Imprint</a>
  </nav>

  <div class="hero-copy abs">
    <div class="intro">My name is</div>
    <div class="name">Jonas</div>
    <div class="role">and I do movies</div>
    <p class="lead">With enthusiasm and wholeheartedly,<br>I am a holistic filmmaker.</p>
  </div>
  <a class="btn" href="#">Read more</a>
</section>
<svg class="torn" style="top:744px;height:22px" viewBox="0 0 1200 22" preserveAspectRatio="none"><path fill="#fff" d="M0 14 L60 10 L130 15 L210 9 L300 13 L380 8 L470 14 L540 11 L620 16 L700 9 L790 13 L860 7 L950 12 L1030 8 L1110 14 L1200 10 L1200 22 L0 22Z"/></svg>

<h2 class="section-title" style="top:808px">My Works</h2>
<div class="work w1" role="img" aria-label="Video still of a woman speaking in a seminar room"><span class="play"></span></div>
<div class="work w2" role="img" aria-label="Video still of a bodywork treatment session"><span class="play"></span></div>
<div class="work w3" role="img" aria-label="Video still of a woman in front of a city tower"><span class="play"></span></div>
<div class="work w4" role="img" aria-label="Video still of a man in a suit"></div>
<a class="btn works-btn" href="#">View all</a>

<section class="journey abs">
  <div class="splash abs" role="img" aria-label="Rainbow coloured powder explosion"></div>
  <h2>Making a movie is always<br>a journey to yourself</h2>
  <p class="p1">Open Heart Films is aimed at all people and institutions whose striving for truthfulness is the driving force behind their actions.</p>
  <p class="p2">I accompany you on the way to portraying your essence, with simple means and without special effects.</p>
  <a class="btn" href="#">Read more</a>
</section>
<svg class="torn" style="top:1316px;height:16px" viewBox="0 0 1200 16" preserveAspectRatio="none"><path fill="#fff" d="M0 0 L1200 0 L1200 8 L1120 12 L1040 6 L950 11 L870 5 L780 10 L690 6 L600 12 L510 7 L420 11 L330 5 L240 10 L150 6 L70 11 L0 7Z"/></svg>
<svg class="torn" style="top:1910px;height:18px" viewBox="0 0 1200 18" preserveAspectRatio="none"><path fill="#fff" d="M0 10 L80 6 L170 12 L260 7 L350 11 L440 5 L530 12 L620 8 L710 13 L800 6 L890 11 L980 7 L1070 12 L1200 8 L1200 18 L0 18Z"/></svg>

<h2 class="section-title" style="top:2008px">Customers</h2>
<div class="clients abs">
  <div class="client">Lumen Haus</div>
  <div class="client"><span class="client-mark"></span>auralis.net</div>
  <div class="client"><span class="client-mark"></span>Sanu Vital</div>
  <div class="client">Klangwerk Festspiele</div>
</div>

<footer class="footer abs">
  <svg class="torn" style="top:-16px;height:18px" viewBox="0 0 1200 18" preserveAspectRatio="none"><path fill="#2e2c2a" d="M0 10 L90 6 L180 12 L260 5 L350 10 L440 6 L520 12 L610 4 L700 11 L790 6 L880 12 L960 5 L1050 10 L1130 6 L1200 9 L1200 18 L0 18Z"/></svg>
  <div class="brand abs">
    <span class="brand-dot"></span>
    <div><div class="brand-name">Jonas Reller</div><div class="brand-tag">Films for the open-hearted</div></div>
  </div>
  <h4 style="left:575px">Quick Links</h4>
  <ul class="links abs"><li>Home</li><li>Offer</li><li>References</li><li>About me</li><li>Imprint</li></ul>
  <h4 style="left:772px">Contact</h4>
  <ul class="contact abs">
    <li><svg width="10" height="14" viewBox="0 0 10 14"><path fill="#f1ece6" d="M5 0a5 5 0 0 0-5 5c0 4 5 9 5 9s5-5 5-9a5 5 0 0 0-5-5zm0 7a2 2 0 1 1 0-4 2 2 0 0 1 0 4z"/></svg><span>Lindenweg 14<br>&nbsp;80331 Munich</span></li>
    <li><svg width="13" height="13" viewBox="0 0 13 13"><path fill="#f1ece6" d="M3 0l2 3-1.4 1.6a8 8 0 0 0 4.8 4.8L10 8l3 2-1 3C5 13 0 8 0 1z"/></svg><span>1 555 010 2040</span></li>
    <li><svg width="16" height="12" viewBox="0 0 16 12"><path fill="#f1ece6" d="M0 0h16v1.5L8 7 0 1.5zM0 3.5l8 5.5 8-5.5V12H0z"/></svg><span>info@jonasreller.com</span></li>
  </ul>
  <div class="divider abs"></div>
  <div class="copy abs">Copyright © 2023, Jonas Reller. All rights reserved.</div>
</footer>

</body>
</html>
```